Personal Training Studio Checkin App (or URL based)

I would like a simple web based app built for our  business. We have a training studio with a simple business model. All our clients buy sessions in packages either 4, 8, or 12 at a time. We want something that a trainer can pull up and Check in a client. This will record the date and time the client was checked in, by what trainer, and what type of session. This system will keep track of the following:
Whenever a Client Checks in so it will ‘tick off’ a session on their package (ie- they have gone from 11 sessions left to 10 sessions left)
Track what sessions a particular trainer does so we can pay them at the end of the week and look at who they trained, what type of session and how many
Look at client activity: Every time they check in, Recharge their package, any activity related to the client, even if it was admin – like deleting a session that was mistakenly recorded.
This will keep a database of clients added and all their activity
The pdf I have included lays out how I think it would work and the features I want
I would like this to run off an tablora that we have at our front check in counter. It can be an app or a URL that use.
***THIS PROJECT IS NOT SO MUCH ABOUT DESIGN BUT ABOUT FUNCTIONALITY OF THE APPLICATION. IT MUST HAVE THE FEATURES I HAVE ASKED FOR THAT WORK TOGETHER. I AM WILLING TO PAY A LITTLE MORE AS A BONUS IF YOU CAN ACCOMPLISH THIS. ALSO IF I FIN THE RIGHT PERSON THAT CAN DO THIS I WILL MAKE IT A GUARNTEED PROJECT.

- Functionality and Track and record all the info we need

```html
<!DOCTYPE html>
<html lang="en">
<head>
<meta charset="utf-8">
<title>Ironpath Training Studio – Check-in App Screens</title>
<link rel="stylesheet" href="https://fonts.googleapis.com/css2?family=Lato:wght@400;700;900&display=swap">
<style>
  :root{
    --orange:#f24a12;
    --orange-dark:#c83a0a;
    --ink:#444;
    --logo-grey:#5a5a5a;
    --panel-dark:#1c1c1c;
    --panel-mid:#3a3a3a;
    --nav-grey:#ececec;
    --white:#ffffff;
  }
  *{box-sizing:border-box;margin:0;padding:0}
  html,body{width:1200px;height:693px;overflow:hidden;background:var(--white);font-family:'Lato',sans-serif}
  .canvas{position:relative;width:1200px;height:693px}
  .screen{position:absolute;width:557px;height:296px;border:2px solid var(--orange);background:var(--white)}
  .screen--home{left:30px;top:32px}
  .screen--checkin{left:610px;top:32px}
  .screen--add{left:30px;top:363px}
  .screen--admin{left:610px;top:363px}

  .brand{position:absolute;display:flex;align-items:center;gap:6px;color:var(--logo-grey);font-weight:900;text-transform:uppercase;line-height:1}
  .brand__mark{width:10px;height:10px;background:var(--orange)}
  .brand--large{left:0;right:0;top:36px;justify-content:center;font-size:38px;gap:10px}
  .brand--large .brand__mark{width:26px;height:26px}
  .brand--small{left:19px;top:18px;font-size:17px}

  .nav{position:absolute;top:15px;left:242px;display:flex;gap:11px}
  .nav__btn{width:92px;height:21px;background:var(--nav-grey);border-bottom:2px solid var(--orange);border-radius:3px;color:var(--ink);font-size:8.5px;display:flex;align-items:center;justify-content:center;white-space:nowrap}
  .nav__btn--active{background:var(--orange);color:var(--white);border-bottom-color:#2a2a2a}

  .panel{position:absolute;border-radius:12px;overflow:hidden;background:var(--panel-dark)}
  .panel__photo{position:absolute;inset:0}
  .panel--home{left:32px;top:130px;width:492px;height:134px}
  .panel--home .panel__photo{background:linear-gradient(120deg,#2c2c2c 0%,#3d3b39 45%,#4a3a36 70%,#333 100%)}
  .panel--form{left:18px;top:68px;width:520px;height:212px}
  .panel--form .panel__photo{background:linear-gradient(135deg,#141414 0%,#262626 50%,#474747 100%)}
  .athlete{position:absolute;left:336px;top:10px;width:162px;height:200px;border-radius:40px;background:radial-gradient(ellipse at 55% 50%,rgba(120,110,100,.35),rgba(40,40,40,0) 70%)}
  .athlete--faint-left{left:20px;top:14px;opacity:.6}
  .athlete--faint-right{left:338px;top:14px;opacity:.6}

  .panel__title{position:absolute;color:var(--orange);font-weight:700;font-size:14px;white-space:nowrap}
  .panel__title--center{left:0;right:0;text-align:center}

  .field{position:absolute;height:22px;background:var(--white);border-radius:2px;color:var(--ink);font-size:8px;display:flex;align-items:center;padding-left:14px}
  .field--select::after{content:"";position:absolute;right:12px;top:9px;border-left:3.5px solid transparent;border-right:3.5px solid transparent;border-top:4px solid #333}

  .btn-submit{position:absolute;width:92px;height:22px;background:var(--orange);border-bottom:2px solid var(--white);border-radius:3px;color:var(--white);font-size:8.5px;font-weight:700;display:flex;align-items:center;justify-content:center}

  .home-btn{position:absolute;top:49px;width:123px;height:29px;border-radius:3px;border-bottom:2px solid var(--orange);background:var(--white);color:var(--ink);font-size:11.5px;display:flex;align-items:center;justify-content:center;white-space:nowrap}
  .home-btn--primary{background:var(--orange);color:var(--white);border-bottom-color:var(--white)}

  .admin-btn{position:absolute;width:124px;height:29px;border-radius:3px;border-bottom:2px solid var(--orange);background:var(--white);color:var(--ink);font-size:11px;display:flex;align-items:center;justify-content:center;white-space:nowrap}
</style>
</head>
<body>
<main class="canvas">

  <!-- Home screen -->
  <section class="screen screen--home">
    <div class="brand brand--large"><span class="brand__mark"></span>Ironpath</div>
    <div class="panel panel--home">
      <div class="panel__photo" role="img" aria-label="Dimmed photo of clients training with equipment in the studio"></div>
      <div class="home-btn home-btn--primary" style="left:47px">CLIENT CHECK IN</div>
      <div class="home-btn" style="left:185px">ADD NEW CLIENT</div>
      <div class="home-btn" style="left:323px">ADMIN PANEL</div>
    </div>
  </section>

  <!-- Client check-in screen -->
  <section class="screen screen--checkin">
    <div class="brand brand--small"><span class="brand__mark"></span>Ironpath</div>
    <nav class="nav">
      <div class="nav__btn nav__btn--active">CLIENT CHECK IN</div>
      <div class="nav__btn">ADD NEW CLIENT</div>
      <div class="nav__btn">ADMIN PANEL</div>
    </nav>
    <div class="panel panel--form">
      <div class="panel__photo"></div>
      <div class="athlete" role="img" aria-label="Photo of an athlete balancing on a kettlebell with arms extended"></div>
      <h2 class="panel__title" style="left:23px;top:25px">CLIENT CHECK IN</h2>
      <div class="field" style="left:23px;top:52px;width:222px">Client Name</div>
      <div class="field field--select" style="left:23px;top:80px;width:222px">Trainer Name</div>
      <div class="field field--select" style="left:23px;top:107px;width:222px">Session Type</div>
      <div class="field" style="left:23px;top:135px;width:222px">Partner Name</div>
      <div class="btn-submit" style="left:23px;top:163px">SUMIT</div>
    </div>
  </section>

  <!-- Add new client screen -->
  <section class="screen screen--add">
    <div class="brand brand--small"><span class="brand__mark"></span>Ironpath</div>
    <nav class="nav">
      <div class="nav__btn">CLIENT CHECK IN</div>
      <div class="nav__btn nav__btn--active">ADD NEW CLIENT</div>
      <div class="nav__btn">ADMIN PANEL</div>
    </nav>
    <div class="panel panel--form">
      <div class="panel__photo" role="img" aria-label="Faint background photo of athletes balancing on kettlebells"></div>
      <h2 class="panel__title panel__title--center" style="top:22px">ADD CLIENT PANEL</h2>
      <div class="field" style="left:23px;top:59px;width:109px">First Name</div>
      <div class="field" style="left:141px;top:59px;width:109px">Last Name</div>
      <div class="field" style="left:270px;top:59px;width:228px">Starting Package Session Amount</div>
      <div class="field" style="left:23px;top:91px;width:109px">Phone</div>
      <div class="field" style="left:141px;top:91px;width:109px">Email</div>
      <div class="field" style="left:270px;top:92px;width:109px">Partner First Name</div>
      <div class="field" style="left:388px;top:92px;width:110px">Partner Last Name</div>
      <div class="field field--select" style="left:23px;top:124px;width:228px">Session Type</div>
      <div class="field" style="left:270px;top:123px;width:109px">Partner Phone</div>
      <div class="field" style="left:388px;top:123px;width:110px">PartnerEmail</div>
      <div class="btn-submit" style="left:215px;top:166px">SUMIT</div>
    </div>
  </section>

  <!-- Admin panel screen -->
  <section class="screen screen--admin">
    <div class="brand brand--small"><span class="brand__mark"></span>Ironpath</div>
    <nav class="nav">
      <div class="nav__btn">CLIENT CHECK IN</div>
      <div class="nav__btn">ADD NEW CLIENT</div>
      <div class="nav__btn nav__btn--active">ADMIN PANEL</div>
    </nav>
    <div class="panel panel--form">
      <div class="panel__photo"></div>
      <div class="athlete athlete--faint-left" role="img" aria-label="Faint photo of an athlete balancing on a kettlebell"></div>
      <div class="athlete athlete--faint-right" role="img" aria-label="Faint mirrored photo of an athlete balancing on a kettlebell"></div>
      <h2 class="panel__title panel__title--center" style="top:48px">ADMIN PANEL</h2>
      <div class="admin-btn" style="left:60px;top:83px">ADD CLIENT</div>
      <div class="admin-btn" style="left:199px;top:83px">CLIENT DETAILS</div>
      <div class="admin-btn" style="left:337px;top:83px">TRAINER REPORT</div>
      <div class="admin-btn" style="left:130px;top:129px">TRAINER PANEL</div>
      <div class="admin-btn" style="left:268px;top:129px">SESSION REPORT</div>
    </div>
  </section>

</main>
</body>
</html>
```